Travel video blogger needs website design

I need a website designed for my new travel video blog "Roaming Sparrow". I have only just started but need a website that is fairly simple and not too busy. I have a logo which I want on it (I have attached it to this project). I also want a link to all my other social medias on the main page (vidtrekhub, Snapwell and Palnook) and my videos as well. Here is a link to my vidtrekhub page for you to look at: https://www.vidtrekhub.net/channel/QRm4tZ8pWnE2HX57YKccd31v
As I have only just started and I am still trying to find my specific niche, again I need it to be sleek and simple that I can go in and change slightly here and there. I would like these pages on the website: About Me, Videos, Social Media, Blog, Gallery, contact me. for an example I like the look of www.theroamingkinfolk.net website.

I already have the domain and I am with Harborweb with pagecraftr.org. I just want to spend my time getting better and learning about videos then trying to create a website (I am a bit of a perfectionist when I try to do something).

Target Market(s)

Young Adults (majority females) between the ages of 18 and 30 with an interest in travelling.

Industry/Entity Type

Travel Industry

Number of Pages Required

1 page

Colors

Designer to choose colors to be used in the design.

Requirements
Must have
• A like to my Snapwell, Palnook and vidtrekhub channels on the home page
• Must be a nice, simple design
• Must have my logo on the front and name "Roaming Sparrow"
Nice to have
• A nice light, bright coloured theme
Should not have
• A dark coloured theme

```html
<!DOCTYPE html>
<html lang="en">
<head>
<meta charset="utf-8">
<title>Roaming Sparrow – My Videos</title>
<link href="https://fonts.googleapis.com/css2?family=Fira+Sans:wght@300;400;600&display=swap" rel="stylesheet">
<style>
  :root {
    --accent: #f2301b;
    --ink: #2b2b2b;
    --nav: #6f6f6f;
    --muted: #9a9a9a;
    --rule: #d6d6d6;
    --bg: #ffffff;
    --social-snap: #7a4a3c;
    --social-pal: #3b5aa0;
    --social-vid: #e53a2c;
  }
  * { margin: 0; padding: 0; box-sizing: border-box; }
  html, body { width: 1200px; height: 1147px; overflow: hidden; background: var(--bg); }
  body { position: relative; font-family: "Fira Sans", Arial, sans-serif; color: var(--ink); }
  a { color: inherit; text-decoration: none; }

  .brand { position: absolute; left: 248px; top: 40px; display: flex; align-items: center; gap: 6px; }
  .brand-dot { width: 10px; height: 10px; border-radius: 50%; background: var(--ink); }
  .brand-name { font-size: 13px; font-weight: 400; letter-spacing: 0.4px; color: var(--ink); text-transform: uppercase; }

  .social { position: absolute; left: 249px; top: 85px; display: flex; gap: 6px; }
  .social a { width: 21px; height: 21px; border-radius: 50%; display: block; }
  .social .snapwell { background: var(--social-snap); }
  .social .palnook { background: var(--social-pal); }
  .social .vidtrekhub { background: var(--social-vid); }

  .main-nav { position: absolute; left: 523px; top: 58px; display: flex; gap: 13.5px; font-size: 14.5px; font-weight: 300; color: var(--nav); }
  .search { position: absolute; left: 934px; top: 59px; }

  .section-title { position: absolute; left: 246px; top: 158px; font-size: 19.5px; font-weight: 600; }
  .section-title span { color: var(--accent); }

  .video-grid { position: absolute; left: 247px; top: 210px; display: grid; grid-template-columns: repeat(3, 180px); column-gap: 84px; grid-auto-rows: 262px; }
  .video-card { width: 180px; }
  .thumb { position: relative; width: 180px; height: 148px; }
  .thumb-mountain { background: linear-gradient(180deg, #3a78c4 0%, #dfe6ef 40%, #6d7178 65%, #2fc2cf 82%, #8d8a86 100%); }
  .thumb-palms { background: linear-gradient(160deg, #b68a4a 0%, #d9b67a 35%, #eef1ec 60%, #9cc4d2 80%, #c49a5a 100%); }
  .thumb-carousel { background: linear-gradient(135deg, #e9552c 0%, #f08a3a 40%, #c8392a 60%, #8ccbe3 80%, #b9dff0 100%); }
  .play { position: absolute; left: 68px; top: 52px; width: 44px; height: 44px; border-radius: 50%; background: rgba(255,255,255,0.72); }
  .play::after { content: ""; position: absolute; left: 17px; top: 13px; border-left: 14px solid var(--accent); border-top: 9px solid transparent; border-bottom: 9px solid transparent; }
  .video-title { font-size: 11.5px; font-weight: 600; line-height: 14.5px; margin-top: 4px; }
  .video-card.tall .video-title { margin-top: 8px; }
  .video-excerpt { font-size: 9.6px; font-weight: 300; color: var(--muted); line-height: 14.5px; margin-top: 8px; width: 180px; }
  .video-card.tall .video-excerpt { margin-top: 6px; margin-left: -2px; }

  .show-more { position: absolute; left: 543px; top: 989px; width: 114px; height: 36px; border-radius: 18px; background: var(--accent); color: #fff; font-size: 13.5px; font-weight: 600; display: flex; align-items: center; justify-content: center; }

  .site-footer { position: absolute; left: 0; top: 1054px; width: 1200px; height: 93px; border-top: 1px solid var(--rule); }
  .footer-brand { position: absolute; left: 248px; top: 44px; display: flex; align-items: center; gap: 6px; }
  .footer-nav { position: absolute; left: 414px; top: 32px; display: flex; align-items: center; font-size: 14px; font-weight: 300; color: var(--nav); }
  .footer-nav .sep { color: var(--accent); margin: 0 8px; font-size: 10px; }
  .copyright { position: absolute; left: 0; width: 1200px; top: 69px; text-align: center; font-size: 8.5px; font-weight: 300; color: var(--muted); padding-left: 0; }
</style>
</head>
<body>
  <header>
    <a class="brand" href="#"><span class="brand-dot"></span><span class="brand-name">Roaming Sparrow</span></a>
    <div class="social">
      <a class="snapwell" href="#" aria-label="Snapwell"></a>
      <a class="palnook" href="#" aria-label="Palnook"></a>
      <a class="vidtrekhub" href="https://www.vidtrekhub.net/channel/QRm4tZ8pWnE2HX57YKccd31v" aria-label="vidtrekhub"></a>
    </div>
    <nav class="main-nav">
      <a href="#">About Me</a><a href="#">Videos</a><a href="#">Social Media</a><a href="#">Blog</a><a href="#">Gallery</a><a href="#">Contact me</a>
    </nav>
    <svg class="search" width="18" height="18" viewBox="0 0 18 18" aria-label="Search">
      <circle cx="7.5" cy="7.5" r="6" fill="none" stroke="#f2301b" stroke-width="1.8"/>
      <line x1="12" y1="12" x2="16.5" y2="16.5" stroke="#f2301b" stroke-width="2" stroke-linecap="round"/>
    </svg>
  </header>

  <main>
    <h1 class="section-title"><span>My</span> Videos</h1>
    <div class="video-grid">
      <article class="video-card">
        <div class="thumb thumb-mountain" role="img" aria-label="Traveller sitting above a turquoise mountain lake"><span class="play"></span></div>
        <h2 class="video-title">Sneak Peek of Next Weeks Video</h2>
        <p class="video-excerpt">Catch a sneak peek of my first video before it goes live next week!</p>
      </article>
      <article class="video-card tall">
        <div class="thumb thumb-palms" role="img" aria-label="Palm trees on a sunny beach"><span class="play"></span></div>
        <h2 class="video-title">Welcome To The Family! (196 days until take off)</h2>
        <p class="video-excerpt">Welcome to my family here at Roaming Sparrow! My name is Maren, I am...</p>
      </article>
      <article class="video-card tall">
        <div class="thumb thumb-carousel" role="img" aria-label="Colourful circus carousel against blue sky"><span class="play"></span></div>
        <h2 class="video-title">I went to the CIRCUS...BY MYSELF!!! (189 days till take off!)</h2>
        <p class="video-excerpt">This week I decided to go to the circus by myself! Originally my sister...</p>
      </article>

      <article class="video-card">
        <div class="thumb thumb-mountain" role="img" aria-label="Traveller sitting above a turquoise mountain lake"><span class="play"></span></div>
        <h2 class="video-title">Sneak Peek of Next Weeks Video</h2>
        <p class="video-excerpt">Catch a sneak peek of my first video before it goes live next week!</p>
      </article>
      <article class="video-card tall">
        <div class="thumb thumb-palms" role="img" aria-label="Palm trees on a sunny beach"><span class="play"></span></div>
        <h2 class="video-title">Welcome To The Family! (196 days until take off)</h2>
        <p class="video-excerpt">Welcome to my family here at Roaming Sparrow! My name is Maren, I am...</p>
      </article>
      <article class="video-card tall">
        <div class="thumb thumb-carousel" role="img" aria-label="Colourful circus carousel against blue sky"><span class="play"></span></div>
        <h2 class="video-title">I went to the CIRCUS...BY MYSELF!!! (189 days till take off!)</h2>
        <p class="video-excerpt">This week I decided to go to the circus by myself! Originally my sister...</p>
      </article>

      <article class="video-card">
        <div class="thumb thumb-mountain" role="img" aria-label="Traveller sitting above a turquoise mountain lake"><span class="play"></span></div>
        <h2 class="video-title">Sneak Peek of Next Weeks Video</h2>
        <p class="video-excerpt">Catch a sneak peek of my first video before it goes live next week!</p>
      </article>
      <article class="video-card tall">
        <div class="thumb thumb-palms" role="img" aria-label="Palm trees on a sunny beach"><span class="play"></span></div>
        <h2 class="video-title">Welcome To The Family! (196 days until take off)</h2>
        <p class="video-excerpt">Welcome to my family here at Roaming Sparrow! My name is Maren, I am...</p>
      </article>
      <article class="video-card tall">
        <div class="thumb thumb-carousel" role="img" aria-label="Colourful circus carousel against blue sky"><span class="play"></span></div>
        <h2 class="video-title">I went to the CIRCUS...BY MYSELF!!! (189 days till take off!)</h2>
        <p class="video-excerpt">This week I decided to go to the circus by myself! Originally my sister...</p>
      </article>
    </div>
    <a class="show-more" href="#">Show More</a>
  </main>

  <footer class="site-footer">
    <a class="footer-brand" href="#"><span class="brand-dot"></span><span class="brand-name">Roaming Sparrow</span></a>
    <nav class="footer-nav">
      <a href="#">About Me</a><span class="sep">•</span><a href="#">Videos</a><span class="sep">•</span><a href="#">Social Media</a><span class="sep">•</span><a href="#">Blog</a><span class="sep">•</span><a href="#">Gallery</a><span class="sep">•</span><a href="#">Contact me</a>
    </nav>
    <p class="copyright">Copyright © 2018 roamingsparrow.net</p>
  </footer>
</body>
</html>
```